Spa Business Card Design Project

Hello! We are a boutique spa for men and women that is rebranding. I would like a memorable new business card that showcases our beautiful new logo and our unique business. I would like it to be classic/timeless and eclectic/artistic at the  same time.
I am a fan of negative space as you can tell from the logo. I am also open to any creative ideas.
Multi sided design. Two sided design is acceptable as an option, too. "Flaps/folds/whatever the design term is" are optional- whether full vertical or horizontal, half flap, full flap etc
On either side next to the golden snail I would potentially like to see "slow down. Enjoy Life."  Possibly on one statment on top of each other, crowned with the snail. Or the statment following the snail on one line... I am open for a creative suprise, too.
The back I would like room for the standard Information
"3817 Birch Lane
Larkhaven, New York 12405
(518) 462 3085
info@thecorvella spa.com
The snail is to be done in gold ink.
Can I also Have an option for cards that are individualized for staff members, too?

Updates
Project Deadline Extended
Reason: I apologize for the deadline extension. My day was more involved than anticipated in other matters. Hope to have this closed by next Tuesday.
Thank you

Target Market(s)
Men and women with expendable income between the ages of 30-55
Industry/Entity Type
Boutique
Requirements
Must have
- only black and gold ink.

Nice to have
- One of a kind.
Showcase the snail :-)
make you smile :-)
Fun, but professional.
Should not have
- Lots of color.
Too feminine.
Too busy.

```html
<!DOCTYPE html>
<html lang="en">
<head>
<meta charset="utf-8">
<title>The Corvella Spa – Card Panels</title>
<link href="https://fonts.googleapis.com/css2?family=Mulish:wght@300;400&display=swap" rel="stylesheet">
<style>
  :root {
    --paper: #ffffff;
    --sand: #eecd98;
    --gold: #d4b07a;
    --gold-line: #c9a56e;
    --ink: #1a1a1a;
    --white: #ffffff;
  }
  * { margin: 0; padding: 0; box-sizing: border-box; }
  html, body { width: 749px; height: 1200px; overflow: hidden; background: var(--paper); }
  body { font-family: "Mulish", "Helvetica Neue", Arial, sans-serif; font-weight: 300; color: var(--ink); }
  .canvas { position: relative; width: 749px; height: 1200px; }
  .panel { position: absolute; }
  .panel--front { left: 0; top: 0; width: 375px; height: 600px; }
  .panel--contact { left: 381px; top: 0; width: 368px; height: 600px; }
  .panel--gallery { left: 0; top: 605px; width: 375px; height: 595px; background: var(--sand); }
  .panel--services { left: 381px; top: 605px; width: 368px; height: 595px; background: var(--sand); }
  .center { position: absolute; left: 0; right: 0; text-align: center; }

  .brand { position: absolute; font-weight: 300; color: var(--ink); text-transform: uppercase; letter-spacing: 2px; line-height: 1; text-align: center; }
  .brand--large { left: 30px; top: 70px; width: 310px; font-size: 40px; }
  .brand--small { left: 0; right: 0; top: 120px; font-size: 15px; letter-spacing: 1px; }
  .brand-tagline { position: absolute; font-weight: 400; color: var(--ink); }
  .brand-tagline--large { left: 58px; top: 201px; font-size: 13.5px; }
  .brand-tagline--small { left: 0; right: 0; top: 158px; font-size: 6px; text-align: center; }

  .mark { position: absolute; width: 26px; height: 26px; border-radius: 50%; background: var(--gold); }
  .motto { font-size: 18px; color: var(--gold); }
  .motto--light { color: var(--white); }

  .rule { position: absolute; height: 2px; }
  .rule--gold { left: 44px; width: 285px; background: linear-gradient(90deg, transparent, var(--gold-line) 20%, var(--gold-line) 80%, transparent); }
  .rule--light { left: 40px; width: 290px; background: linear-gradient(90deg, transparent, rgba(255,255,255,.9) 20%, rgba(255,255,255,.9) 80%, transparent); }

  .contact-phone { top: 214px; font-size: 26px; }
  .contact-email { top: 256px; font-size: 22px; }
  .contact-address { top: 294px; font-size: 20px; line-height: 28px; }

  .photo { position: absolute; left: 87px; width: 193px; height: 136px; }
  .photo--massage { top: 52px; background: linear-gradient(160deg, #f6f1ea 0%, #e2b48a 45%, #c58a5b 100%); }
  .photo--stones { top: 223px; background: linear-gradient(170deg, #d7d2cc 0%, #9a6bb0 35%, #6b8a55 60%, #d9dcd8 100%); }
  .photo--lounge { top: 397px; background: linear-gradient(135deg, #a88a5c 0%, #d8c29a 45%, #e9e1cf 70%, #8a6a40 100%); }

  .services-title { top: 62px; font-size: 46px; font-weight: 300; color: var(--white); }
  .services-list { top: 170px; list-style: none; color: var(--white); font-size: 31px; line-height: 40.5px; }
</style>
</head>
<body>
<main class="canvas">

  <section class="panel panel--front">
    <div class="brand brand--large">The<br>Corvella<br>Spa</div>
    <div class="brand-tagline brand-tagline--large">a boutique spa for Men &amp; Women</div>
    <span class="mark" style="left:178px; top:508px;"></span>
    <p class="center motto" style="top:546px; width:390px;">Slow down • Enjoy life</p>
  </section>

  <section class="panel panel--contact">
    <div class="brand brand--small">The Corvella Spa</div>
    <div class="brand-tagline brand-tagline--small">a boutique spa for Men &amp; Women</div>
    <div class="rule rule--gold" style="top:192px;"></div>
    <p class="center contact-phone">P: (518) 462 3085</p>
    <p class="center contact-email">E: info@thecorvella spa.com</p>
    <p class="center contact-address">3817 Birch Lane<br>Larkhaven, New York 12405</p>
    <div class="rule rule--gold" style="top:369px;"></div>
    <span class="mark" style="left:172px; top:411px;"></span>
    <p class="center motto" style="top:450px;">Slow down • Enjoy life</p>
  </section>

  <section class="panel panel--gallery">
    <div class="photo photo--massage" role="img" aria-label="Photo of hands giving a back massage"></div>
    <div class="photo photo--stones" role="img" aria-label="Photo of pink and purple flowers with spa stones and candles"></div>
    <div class="photo photo--lounge" role="img" aria-label="Photo of a bright spa lounge with robes and a chair"></div>
  </section>

  <section class="panel panel--services">
    <h2 class="center services-title">Services</h2>
    <div class="rule rule--light" style="top:139px;"></div>
    <ul class="center services-list">
      <li>Massage</li>
      <li>Facials</li>
      <li>Hand &amp; Foot care</li>
      <li>Electrolysis</li>
      <li>Waxing</li>
      <li>Bridal</li>
    </ul>
    <div class="rule rule--light" style="top:442px;"></div>
    <span class="mark" style="left:172px; top:520px; background:var(--white);"></span>
    <p class="center motto motto--light" style="top:552px;">Slow down • Enjoy life</p>
  </section>

</main>
</body>
</html>
```